Retail Jewelry Business Card Design Project

We are in need of a new business card design for a retail jewelry store. This store is in the business of fine jewelry including but not specific to bridal jewelry, diamonds, designer jewelry and watches.

This store has been in business for 20 years but continues to strive for a modern professional appeal. The main colors use for this business are a royal blue, white and silver.

Target Market(s)

Target market is ages 18-50

Industry/Entity Type

Jewelry

Requirements
Must have
• Sales Person Name
Sales Person Email Address

Store Address
Store Phone
Website

Standard business card size. No odd shapes or sizes.
Nice to have
• Overall modern feel for card.

We have thought that a design with a nice feature of the logo on the back of the card would be nice but open to ideas.
Should not have
• No specific images of jewelry should be used.

```html
<!DOCTYPE html>
<html lang="en">
<head>
<meta charset="utf-8">
<title>Mara Linden Fine Jewelry – Business Card</title>
<link href="https://fonts.googleapis.com/css2?family=Crimson+Text:ital,wght@0,400;0,600;1,400&display=swap" rel="stylesheet">
<style>
  :root {
    --page: #ffffff;
    --navy: #0a1a40;
    --navy-edge: #101c4a;
    --royal: #1d1a8a;
    --royal-rule: #6a5fb8;
    --silver: #8d8d8d;
    --rule: #5f6a8c;
    --ink-light: #ffffff;
    --faint: rgba(255, 255, 255, 0.055);
  }
  * { margin: 0; padding: 0; box-sizing: border-box; }
  html, body {
    width: 1200px; height: 847px; overflow: hidden;
    background: var(--page);
    font-family: "Crimson Text", Georgia, serif;
  }
  .canvas { position: relative; width: 1200px; height: 847px; }

  .card { position: absolute; overflow: hidden; }

  /* Front */
  .card-front {
    left: 355px; top: 96px; width: 503px; height: 287px;
    background: radial-gradient(ellipse 62% 62% at 49% 50%, #ffffff 0%, #e6e6f0 18%, #9ea2c8 45%, #3a4a86 75%, var(--navy-edge) 100%);
    box-shadow: 10px 10px 12px rgba(0, 0, 0, 0.45);
  }
  .front-name {
    position: absolute; left: 0; right: 0; top: 78px;
    text-align: center; color: var(--royal);
    font-weight: 600; font-size: 66px; line-height: 1; white-space: nowrap;
  }
  .front-rule {
    position: absolute; left: 78px; width: 350px; top: 162px;
    height: 2px; background: var(--royal-rule);
  }
  .front-tag {
    position: absolute; left: 0; right: 0; top: 166px;
    text-align: center; color: var(--royal);
    font-weight: 600; font-size: 25px; letter-spacing: 3px; white-space: nowrap;
  }

  /* Back */
  .card-back {
    left: 355px; top: 449px; width: 505px; height: 290px;
    background: var(--navy);
  }
  .back-name-mark {
    position: absolute; left: 30px; top: 18px; width: 210px;
    color: var(--silver); font-weight: 600; text-align: center; white-space: nowrap;
  }
  .back-name-mark .mark-name { font-size: 38px; line-height: 1; }
  .back-name-mark .mark-tag { font-size: 14px; letter-spacing: 1.5px; border-top: 2px solid var(--silver); padding-top: 1px; margin-top: 4px; }

  .backdrop-name {
    position: absolute; left: 0; top: 78px; width: 505px;
    color: var(--faint); font-weight: 600; text-align: center; white-space: nowrap;
  }
  .backdrop-name .mark-name { font-size: 90px; line-height: 1; }
  .backdrop-name .mark-tag { font-size: 30px; line-height: 1; letter-spacing: 4px; margin-top: 14px; }

  .frame { position: absolute; left: 0; top: 0; }

  .contact {
    position: absolute; left: 252px; color: var(--ink-light);
    font-style: italic; font-size: 21px; line-height: 1; white-space: nowrap;
  }
  .contact-person { top: 89px; }
  .contact-street { top: 133px; }
  .contact-city { top: 162px; }
  .contact-email { top: 196px; left: 194px; display: flex; align-items: center; gap: 6px; }

  .web-pill {
    position: absolute; left: 86px; top: 243px; width: 312px; height: 31px;
    border: 2px solid var(--rule); border-radius: 10px;
    color: var(--ink-light); font-style: italic; font-size: 22px;
    text-align: center; line-height: 26px; white-space: nowrap;
  }
</style>
</head>
<body>
<div class="canvas">

  <section class="card card-front" aria-label="Card front">
    <div class="front-name">Mara Linden</div>
    <div class="front-rule"></div>
    <div class="front-tag">FINE JEWELRY</div>
  </section>

  <section class="card card-back" aria-label="Card back">
    <div class="backdrop-name" aria-hidden="true">
      <div class="mark-name">Mara Linden</div>
      <div class="mark-tag">FINE JEWELRY</div>
    </div>

    <div class="back-name-mark">
      <div class="mark-name">Mara Linden</div>
      <div class="mark-tag">FINE JEWELRY</div>
    </div>

    <svg class="frame" width="505" height="290" aria-hidden="true">
      <g stroke="#5f6a8c" stroke-width="2">
        <line x1="13" y1="129" x2="493" y2="129"/>
        <line x1="13" y1="234" x2="493" y2="234"/>
        <line x1="28" y1="117" x2="28" y2="246"/>
        <line x1="478" y1="117" x2="478" y2="246"/>
      </g>
    </svg>

    <div class="contact contact-person">Owen Merrick Hale</div>
    <div class="contact contact-street">2210 Bayview Avenue</div>
    <div class="contact contact-city">Port Adele, FL 32490</div>
    <div class="contact contact-email">
      <svg width="18" height="14" viewBox="0 0 18 14" aria-hidden="true">
        <g transform="rotate(-15 9 7)">
          <rect x="1" y="2" width="16" height="10" fill="#ffffff"/>
          <polyline points="1,2 9,8 17,2" fill="none" stroke="#9aa0b8" stroke-width="1"/>
        </g>
      </svg>
      <span>owen@maralindenjewelry.com</span>
    </div>

    <div class="web-pill">www.maralindenjewelry.com</div>
  </section>

</div>
</body>
</html>
```